computter lessons

new business venture [ self employed ] will register my business name as " KEYVORLAN "
what I will offer is :-
computer lessons for new beginners.
Initial set up and basic overview.
lessons per hour in the comfort of your own home.
special rates for customers aged 50+
First lesson is half price with no obligation for booking any further appointments.
a learning and training plan will be presented based on your requirements.
an appraisal update on your new skills.

contact info:-
0161 4970213
07700 900482
larkden@mervoxmail.com

```html
<!DOCTYPE html>
<html lang="en">
<head>
<meta charset="utf-8">
<title>KEYVORLAN – Computer Lessons Flyer</title>
<link href="https://fonts.googleapis.com/css2?family=Arimo:wght@400;700&display=swap" rel="stylesheet">
<style>
  :root{
    --backdrop:#6b6b6d;
    --navy-deep:#121d35;
    --navy:#1c3358;
    --blue-mid:#1f5f9c;
    --blue-glow:#3fa2e0;
    --sky:#5fd0f5;
    --bubble-top:#7fd3f7;
    --bubble-bottom:#1670b8;
    --yellow:#ffe600;
    --orange:#f47b20;
    --white:#ffffff;
    --light-blue:#8fd3ff;
  }
  *{box-sizing:border-box;margin:0;padding:0}
  html,body{width:1200px;height:892px;overflow:hidden}
  body{
    background:var(--backdrop);
    font-family:"Arimo",Arial,sans-serif;
    position:relative;
  }
  .flyer{
    position:absolute;left:300px;top:22px;width:600px;height:848px;
    overflow:hidden;
    background:
      radial-gradient(ellipse 70% 40% at 55% 40%, rgba(63,162,224,.55), transparent 70%),
      linear-gradient(180deg,var(--navy) 0%,var(--blue-mid) 42%,var(--navy) 68%,var(--navy-deep) 100%);
    box-shadow:0 10px 30px rgba(0,0,0,.45);
  }
  .swoosh{position:absolute;left:0;top:330px;width:600px;height:190px}
  .brand{
    position:absolute;top:36px;right:40px;
    display:flex;align-items:center;gap:8px;
    font-weight:700;font-size:28px;letter-spacing:2px;color:var(--sky);
  }
  .brand-mark{width:14px;height:14px;background:var(--sky)}
  .computer-art{
    position:absolute;left:165px;top:95px;width:270px;height:215px;border-radius:10px;
    background:linear-gradient(160deg,#4a5d78 0%,#26344a 55%,#8fa3b8 100%);
  }
  .topic{
    position:absolute;border-radius:50%;
    display:flex;align-items:center;justify-content:center;text-align:center;
    color:var(--white);font-weight:700;font-size:15px;line-height:1.15;
    background:radial-gradient(circle at 50% 20%,var(--bubble-top),var(--bubble-bottom) 75%);
    border:2px solid rgba(255,255,255,.75);
    box-shadow:0 4px 10px rgba(0,0,0,.35);
  }
  .topic--email{left:42px;top:225px;width:100px;height:100px}
  .topic--internet{left:88px;top:322px;width:112px;height:112px}
  .topic--web{left:245px;top:338px;width:112px;height:112px}
  .topic--ebooks{left:352px;top:292px;width:112px;height:112px}
  .topic--intro{left:440px;top:162px;width:112px;height:112px}
  .home-badge{
    position:absolute;left:472px;top:300px;width:108px;height:108px;border-radius:50%;
    background:var(--yellow);color:#1a1a1a;
    display:flex;align-items:center;justify-content:center;text-align:center;
    font-weight:700;font-size:12px;line-height:1.2;padding:10px;
  }
  .headline{
    position:absolute;left:30px;top:470px;width:380px;
    color:var(--yellow);font-weight:700;font-size:30px;
  }
  .subhead{
    position:absolute;left:30px;top:508px;width:380px;
    color:var(--white);font-weight:700;font-size:14px;
  }
  .photo{position:absolute;border:2px solid var(--white)}
  .photo--class{left:30px;top:572px;width:168px;height:96px;background:linear-gradient(135deg,#c9d3dd,#5d6f86)}
  .photo--tutor{left:206px;top:540px;width:184px;height:128px;background:linear-gradient(135deg,#e9edf1,#6e7d92)}
  .photo--home{left:400px;top:448px;width:176px;height:128px;background:linear-gradient(135deg,#d8b7a3,#a33b3b)}
  .age-tag{
    position:absolute;left:418px;top:590px;width:168px;height:46px;
    background:var(--orange);color:var(--white);
    clip-path:polygon(10% 0,100% 0,100% 100%,10% 100%,0 50%);
    display:flex;align-items:center;justify-content:center;text-align:center;
    font-weight:700;font-size:12px;line-height:1.2;padding-left:14px;
  }
  .details{position:absolute;left:30px;top:684px;width:545px;font-weight:700}
  .details p{line-height:1.3}
  .details .offer{color:var(--yellow);font-size:15px}
  .details .experience{color:var(--light-blue);font-size:15px}
  .details .plan{color:var(--white);font-size:13px;margin-top:10px}
  .details .rule{height:1px;background:rgba(255,255,255,.6);margin:8px 0}
  .details .contact{color:var(--white);font-size:13px}
</style>
</head>
<body>
  <main class="flyer">
    <svg class="swoosh" viewBox="0 0 600 190" aria-hidden="true">
      <path d="M0 120 C150 40 350 160 600 60 L600 90 C360 190 160 70 0 150Z" fill="rgba(95,208,245,.35)"/>
      <path d="M0 90 C180 20 380 130 600 30" stroke="rgba(255,255,255,.5)" stroke-width="2" fill="none"/>
      <path d="M0 150 C200 90 400 170 600 110" stroke="rgba(143,211,255,.45)" stroke-width="3" fill="none"/>
    </svg>

    <div class="brand"><span class="brand-mark"></span>KEYVORLAN</div>

    <div class="computer-art" role="img" aria-label="Desktop computer with monitor showing a world map, tower, keyboard and mouse"></div>

    <div class="topic topic--email">Email<br>Basics</div>
    <div class="topic topic--internet">Internet<br>Navigation</div>
    <div class="topic topic--web">Smart use<br>of the web</div>
    <div class="topic topic--ebooks">Introduction<br>to eBooks</div>
    <div class="topic topic--intro">Intro to<br>Computers</div>
    <div class="home-badge">lessons per hour in the comfort of your own home.</div>

    <h1 class="headline">Its right time to Upgrade?</h1>
    <p class="subhead">Basic Computer Teaching Class for New beginners.</p>

    <div class="photo photo--class" role="img" aria-label="Photo of students learning at computers in a classroom"></div>
    <div class="photo photo--tutor" role="img" aria-label="Photo of a tutor helping an older learner at a computer"></div>
    <div class="photo photo--home" role="img" aria-label="Photo of a family using a laptop at home"></div>
    <div class="age-tag">special rates for<br>customers aged 50+</div>

    <section class="details">
      <p class="offer">Reserve your 1 hour Training Session Now!!</p>
      <p class="offer">Advanced Classes Available upon request.</p>
      <p class="experience">28 years experience in the infrastructure<br>and computer networking industry</p>
      <p class="plan">A tailor made learning and training plan. | An appraisal update on your new skills.</p>
      <div class="rule"></div>
      <p class="contact">contact info:- 0161 4970213 | 07700 900482 | larkden@mervoxmail.com</p>
    </section>
  </main>
</body>
</html>
```